Events Online Video Streaming Company

A website needs to be designed to replace the current website of a company that specialises in providing an online portal for streaming events to users. the current portal exists at: http://www.tazorin.com <- designers can get a "feel" for what they do and the content they require from this existing website.
the current tazorin logo and green color are to be maintined. i will upload an EPS of the logo soon.
The new design needs to highlight the main aspects of what they do: live streaming of events, multiple cameras, online chat, user activity data (like brindle metrics), customised front-ends.
we want the design to be in-between a corporate feel and modern, contemporary. ie. we dont want it to be too corporate (like the current website).
the design must also incorporate the word: fernoskaps as part of their slogan or sub-title.
hi everyone,

```html
<!DOCTYPE html>
<html lang="en">
<head>
<meta charset="utf-8">
<title>tazorin – fernoskaps</title>
<link href="https://fonts.googleapis.com/css2?family=Montserrat:wght@300;400;500;600&display=swap" rel="stylesheet">
<style>
:root{
  --green:#8cc63e;
  --green-dark:#7db236;
  --footer:#9dc54b;
  --footer-bar:#96bf45;
  --ink:#2a2a2a;
  --muted:#808080;
  --panel:#f4f4f4;
  --line:#e2e2e2;
  --white:#ffffff;
  --edu:#1ba9e1;
  --sport:#22a84a;
  --comms:#6b3597;
  --gig:#d4187a;
  --conf:#f6b80f;
  --other:#555555;
}
*{box-sizing:border-box;margin:0;padding:0}
html,body{width:1200px;height:2228px;overflow:hidden}
body{font-family:"Montserrat",Arial,sans-serif;color:var(--ink);background:var(--white);position:relative}
a{color:inherit;text-decoration:none}

.top-strip{position:absolute;left:0;top:0;width:1200px;height:24px;background:#111}

.hero{position:absolute;left:0;top:24px;width:1200px;height:537px;overflow:hidden}
.hero-scene{position:absolute;inset:0;background:linear-gradient(180deg,#a9cdf0 0%,#c9e1f6 55%,#dcebf5 78%,#7fae3a 86%,#5c8f24 100%)}
.brand{position:absolute;left:137px;top:22px}
.brand-name{font-size:48px;font-weight:500;color:var(--green);letter-spacing:-1px;line-height:1}
.brand-tag{display:block;font-size:14px;font-weight:400;color:#555;text-align:right;margin-top:2px;font-style:normal}
.main-nav{position:absolute;right:131px;top:56px;display:flex;font-size:16px;color:#444}
.main-nav a{padding:0 14px;border-left:1px solid #777;line-height:16px}
.main-nav a:first-child{border-left:0}
.main-nav a:last-child{padding-right:0}
.hero-title{position:absolute;left:610px;top:276px;font-size:29px;font-weight:400;line-height:39px;color:#111}
.hero-title span{color:var(--green)}

.welcome{position:absolute;left:0;top:561px;width:1200px;height:84px;background:var(--panel);border-bottom:1px solid var(--line);display:flex;align-items:center;justify-content:center;gap:20px}
.welcome p{font-size:19px;color:#333}
.btn{display:inline-block;background:var(--green);color:var(--white);font-size:18px;font-weight:500;width:169px;height:48px;line-height:48px;text-align:center;border-bottom:2px solid var(--green-dark)}

.services{position:absolute;left:0;top:645px;width:1200px;height:315px;background:var(--panel);border-bottom:1px solid var(--line)}
.service-card{position:absolute;top:38px;width:218px;height:211px;background:var(--white);padding:18px 15px;box-shadow:0 10px 12px -8px rgba(0,0,0,.18)}
.service-card h3{font-size:11px;font-weight:500;color:var(--green);letter-spacing:.3px;margin-bottom:26px}
.service-card p{font-size:11px;line-height:22px;color:var(--muted);text-align:justify;font-weight:300}
.pager{position:absolute;left:575px;display:flex;gap:9px}
.pager span{width:21px;height:21px;border-radius:50%;display:block}
.pager .prev{background:var(--green)}
.pager .next{background:#333}
.pager svg{display:block}

.apps{position:absolute;left:0;top:960px;width:1200px;height:513px;background:var(--white);border-bottom:1px solid var(--line)}
.app{position:absolute;width:300px;text-align:center}
.app-icon{display:block;width:82px;height:82px;margin:0 auto;border-radius:6px}
.app h3{font-size:14px;font-weight:500;margin-top:26px}
.app p{font-size:12px;line-height:24px;color:#666;margin-top:6px;font-weight:300}

.features{position:absolute;left:0;top:1473px;width:1200px;height:422px;background:var(--panel)}
.feature{position:absolute;top:82px;width:219px}
.feature-media{height:125px}
.feature h3{font-size:14px;font-weight:400;color:#222;margin-top:20px;letter-spacing:.3px}
.feature p{font-size:11px;line-height:24px;color:var(--muted);text-align:justify;margin-top:6px;font-weight:300}

.site-footer{position:absolute;left:0;top:1895px;width:1200px;height:263px;background:var(--footer);color:var(--white)}
.foot-col{position:absolute;top:28px}
.foot-col h4{font-size:11px;font-weight:500;line-height:16px;margin-bottom:14px}
.foot-col li{list-style:none;font-size:11px;line-height:24px;font-weight:400}
.foot-divider{position:absolute;left:890px;top:0;width:1px;height:263px;background:rgba(255,255,255,.35)}
.newsletter{width:230px;height:230px}
.newsletter p{font-size:11px;line-height:20px;width:225px}
.field{position:absolute;left:0;width:221px;height:27px;background:#f2f2f2;font-size:10px;color:#999;padding-left:12px;line-height:27px}
.field.name{top:85px}
.field.mail{top:128px}
.subscribe{position:absolute;left:123px;top:173px;width:98px;height:23px;border-radius:12px;background:#3f6512;color:var(--white);font-size:11px;line-height:23px;text-align:center}
.social li{display:flex;justify-content:space-between;align-items:center;width:140px;line-height:38px}
.social .dot{width:26px;height:26px;border-radius:50%;background:var(--white);display:block}
.legal-bar{position:absolute;left:0;top:2158px;width:1200px;height:70px;background:var(--footer-bar);border-top:1px solid rgba(255,255,255,.3);display:flex;align-items:center;justify-content:center;color:var(--white);font-size:11px;font-weight:500;gap:12px}
</style>
</head>
<body>
<div class="top-strip"></div>

<header class="hero">
  <div class="hero-scene" role="img" aria-label="Woman sitting on green grass with a laptop under a clear blue sky"></div>
  <div class="brand">
    <div class="brand-name">tazorin</div>
    <em class="brand-tag">fernoskaps</em>
  </div>
  <nav class="main-nav">
    <a href="#">Home</a><a href="#">Features</a><a href="#">Applications</a><a href="#">The Team</a><a href="#">Support</a><a href="#">Contact us</a>
  </nav>
  <h1 class="hero-title">We are an online portal for<br><span>streaming events to users.</span></h1>
</header>

<section class="welcome">
  <p>Welcome to Tazorin a live social media integrated portal</p>
  <a class="btn" href="#">Contact Us</a>
</section>

<section class="services">
  <article class="service-card" style="left:131px">
    <h3>INNOVATION / TECHNOLOGY</h3>
    <p>Developments such as mobile devices, mobile internet, video streaming, cloud computing, and web development systems have made it possible for us to develop Tazorin ...</p>
  </article>
  <article class="service-card" style="left:370px">
    <h3>SOCIAL MEDIA, NETWORKING</h3>
    <p>Users can engage with the event by integrating their existing social networking accounts allowing them to see their connections and establish professional ...</p>
  </article>
  <article class="service-card" style="left:609px">
    <h3>LIVE VIDEO STREAMING</h3>
    <p>High quality live video streaming means you get to see the event as it happens without waiting for a stream to buffer. Tazorin offers a choice of different resolutions ...</p>
  </article>
  <article class="service-card" style="left:849px">
    <h3>VIDEO ON DEMAND</h3>
    <p>4Video on demand is available almost immediately after each session of the event, or as part of a media library so you can watch the video when ever you want ...</p>
  </article>
  <div class="pager" style="top:276px">
    <span class="prev"><svg width="21" height="21" viewBox="0 0 21 21"><path d="M12 6l-4 4.5 4 4.5" fill="none" stroke="#fff" stroke-width="2"/></svg></span>
    <span class="next"><svg width="21" height="21" viewBox="0 0 21 21"><path d="M9 6l4 4.5-4 4.5" fill="none" stroke="#fff" stroke-width="2"/></svg></span>
  </div>
</section>

<section class="apps">
  <div class="app" style="left:131px;top:26px">
    <span class="app-icon" style="background:var(--edu)"></span>
    <h3 style="color:var(--edu)">Education</h3>
    <p>With much of todays learning being based<br>off campus, Tazorin is an effective educa-<br>tional tool.</p>
  </div>
  <div class="app" style="left:448px;top:26px">
    <span class="app-icon" style="background:var(--sport)"></span>
    <h3 style="color:var(--sport)">Sport</h3>
    <p>With much of todays learning being based<br>off campus, Tazorin is an effective educa-<br>tional tool.</p>
  </div>
  <div class="app" style="left:769px;top:26px">
    <span class="app-icon" style="background:var(--comms)"></span>
    <h3 style="color:var(--comms)">Education</h3>
    <p>With much of todays learning being based<br>off campus, Tazorin is an effective educa-<br>tional tool.</p>
  </div>
  <div class="app" style="left:131px;top:247px">
    <span class="app-icon" style="background:var(--gig)"></span>
    <h3 style="color:var(--gig)">Education</h3>
    <p>With much of todays learning being based<br>off campus, Tazorin is an effective educa-<br>tional tool.</p>
  </div>
  <div class="app" style="left:448px;top:247px">
    <span class="app-icon" style="background:var(--conf)"></span>
    <h3 style="color:var(--conf)">Education</h3>
    <p>With much of todays learning being based<br>off campus, Tazorin is an effective educa-<br>tional tool.</p>
  </div>
  <div class="app" style="left:769px;top:247px">
    <span class="app-icon" style="background:var(--other)"></span>
    <h3 style="color:var(--other)">Education</h3>
    <p>With much of todays learning being based<br>off campus, Tazorin is an effective educa-<br>tional tool.</p>
  </div>
</section>

<section class="features">
  <article class="feature" style="left:131px">
    <div class="feature-media" role="img" aria-label="Glowing padlock on a blue circuit board" style="background:linear-gradient(135deg,#0b2e8a,#2f6ee0 50%,#0a2a7a)"></div>
    <h3>SECURE EVENT CONTENT</h3>
    <p>Tazorin allows event organisers to diversify their event income streams by adding revenue from virtual delegates as well as industry partners or sponsors of the event portal.</p>
  </article>
  <article class="feature" style="left:370px">
    <div class="feature-media" role="img" aria-label="Close-up of a circuit board with a chip" style="background:linear-gradient(135deg,#1d3550,#5a86a8 50%,#1a2d44)"></div>
    <h3>LATEST TECHNOLOGY</h3>
    <p>Tazorin allows event organisers to diversify their event income streams by adding revenue from virtual delegates as well as industry partners or sponsors of the event portal.</p>
  </article>
  <article class="feature" style="left:609px">
    <div class="feature-media" role="img" aria-label="Busy businessman juggling phones and a laptop" style="background:linear-gradient(180deg,#e9ecef,#b8bec4 60%,#3a3d42)"></div>
    <h3>TOO BUSY TO ATTEND?</h3>
    <p>Tazorin allows event organisers to diversify their event income streams by adding revenue from virtual delegates as well as industry partners or sponsors of the event portal.</p>
  </article>
  <article class="feature" style="left:849px">
    <div class="feature-media" role="img" aria-label="Silhouetted crowd cheering with raised hands" style="background:linear-gradient(180deg,#f2d9a0,#c99a4c 45%,#1a1208 75%)"></div>
    <h3>GLOBAL AUDIENCE</h3>
    <p>Tazorin allows event organisers to diversify their event income streams by adding revenue from virtual delegates as well as industry partners or sponsors of the event portal.</p>
  </article>
  <div class="pager" style="top:379px">
    <span class="prev"><svg width="21" height="21" viewBox="0 0 21 21"><path d="M12 6l-4 4.5 4 4.5" fill="none" stroke="#fff" stroke-width="2"/></svg></span>
    <span class="next"><svg width="21" height="21" viewBox="0 0 21 21"><path d="M9 6l4 4.5-4 4.5" fill="none" stroke="#fff" stroke-width="2"/></svg></span>
  </div>
</section>

<footer class="site-footer">
  <div class="foot-col" style="left:131px">
    <h4>Quick Links</h4>
    <ul><li>Welcome!</li><li>Features</li><li>Applications</li><li>The Team</li><li>Support</li><li>Contact Us</li></ul>
  </div>
  <div class="foot-col" style="left:291px">
    <h4>Support Links</h4>
    <ul><li>Legal Notice</li><li>Privacy Policy</li><li>Terms &amp; Conditions</li><li>Help</li></ul>
  </div>
  <div class="foot-col" style="left:451px">
    <h4>Support Links</h4>
    <ul><li>Communications</li><li>Conferences and</li><li>conventions</li><li>Education and</li><li>training</li><li>Festivals and Gigs</li><li>Live video streaming</li><li>Sporting Events</li></ul>
  </div>
  <div class="foot-col newsletter" style="left:609px">
    <h4>Newsletter SignUp</h4>
    <p>Sign-up for our daily emails by<br>entering your information below:</p>
    <span class="field name">Name</span>
    <span class="field mail">E-Mail ID</span>
    <a class="subscribe" href="#">Subscribe</a>
  </div>
  <div class="foot-divider"></div>
  <div class="foot-col social" style="left:933px">
    <h4 style="margin-bottom:6px">Connect With Us</h4>
    <ul><li>Flitter<span class="dot"></span></li><li>Circlebook<span class="dot"></span></li><li>Linkwork<span class="dot"></span></li></ul>
  </div>
</footer>

<div class="legal-bar">
  <span>©2013 Company Name , All Rights Reserved</span><span>|</span><span>Privacy Policy</span><span>|</span><span>Terms &amp; Conditions</span>
</div>
</body>
</html>
```